Marigold Haven - Foundation PPT

Design a cohesive, emotionally resonant PowerPoint template that reflects the heart of Marigold Haven Pregnancy & Family Support. This template will be used across fundraising, partnership, and storytelling presentations, and must balance professionalism with warmth, compassion, and human connection.

Background
Marigold Haven Pregnancy & Family Support exists to support families navigating complicated pregnancies, prolonged hospital stays, and loss. The brand is rooted in empathy, quiet strength, and the concept of a “web” of care—an interconnected support system that surrounds families during difficult moments.

The template should feel deeply personal and mission-driven, not corporate.

Design Goals
Create a visually cohesive slide system that can be reused across multiple presentation types

Capture the emotional tone of the organization:
-Warm
-Gentle
-Hopeful
-Supportive
Ensure the design is clean, minimal, and easy to use for non-designers
Maintain a balance between storytelling and credibility

Key Design Requirements
-Brand Integration: Incorporate the Marigold Haven logo (provided)
Align with soft, neutral color palette (e.g., cream, sage, blush, light sky tones)
-Use elegant, readable typography

Slide Templates to Include
-Cover Slide (emotion-forward, minimal text)
-Mission / Story Slide
-Program Overview Slide
-Impact / Metrics Slide
-Partnership / Sponsor Slide
-“Web of Support” Concept Slide (visual representation of interconnected care)
-Call to Action Slide
-Optional: Quote/Testimonial Slide

Visual Style
-Soft, calming, and approachable aesthetic
-Use of whitespace to avoid clutter
-Light use of icons or illustrations (if applicable)
-Avoid overly corporate or overly busy design elements

Usability
-Fully editable in PowerPoint
-Clear text hierarchy and placeholders
-Easy for internal team to update content without design support
-Tone & Emotional Direction

This is not a clinical or corporate presentation—it should feel human, heartfelt, and intentional.

website: https://www.marigoldhavencare.org

```html
<!DOCTYPE html>
<html lang="en">
<head>
<meta charset="utf-8">
<title>Marigold Haven – Foundation Presentation Template</title>
<link href="https://fonts.googleapis.com/css2?family=Marcellus&family=Roboto:wght@400;500;700&display=swap" rel="stylesheet">
<style>
:root{
  --stage:#8f8f8f;
  --plum:#7b4fa6;
  --plum-dark:#5e3a8a;
  --lilac:#b99ad6;
  --lilac-soft:#e9dcf5;
  --mist:#f8f4fc;
  --ink:#3b3346;
  --muted:#6a6274;
  --white:#ffffff;
  --gold:#e0a526;
  --serif:'Marcellus', serif;
  --sans:'Roboto', sans-serif;
}
*{box-sizing:border-box;margin:0;padding:0}
html,body{width:1124px;height:1200px;overflow:hidden}
body{background:var(--stage);position:relative;font-family:var(--sans);color:var(--ink)}
.slide{position:absolute;width:447px;height:251px;overflow:hidden;
  background:linear-gradient(180deg,var(--mist) 0%,#f1e8f8 55%,var(--lilac-soft) 100%);
  box-shadow:0 4px 10px rgba(0,0,0,.25)}
.col-a{left:109px}.col-b{left:567px}
.row-1{top:78px}.row-2{top:342px}.row-3{top:606px}.row-4{top:870px}
.abs{position:absolute}
.slide-title{position:absolute;left:26px;top:9px;font-family:var(--serif);font-size:17px;color:var(--plum)}
/* brand lockup */
.brand{position:absolute;display:flex;align-items:center;gap:4px}
.brand-dot{border-radius:50%;border:1px solid currentColor;flex:none}
.brand-name{font-family:var(--serif);line-height:1}
.brand-tag{font-family:var(--sans);letter-spacing:.06em;line-height:1;margin-top:2px}
.brand-sm{right:16px;top:12px;color:var(--plum)}
.brand-sm .brand-dot{width:9px;height:9px}
.brand-sm .brand-name{font-size:11px}
.brand-sm .brand-tag{font-size:3.6px}
/* footer */
.footer{position:absolute;left:0;bottom:0;width:100%;height:16px;background:var(--plum);
  border-radius:8px 8px 0 0;display:flex;align-items:center;padding:0 12px 0 30px;color:var(--white);font-size:5.4px}
.footer .item{display:flex;align-items:center;gap:3px;margin-right:10px}
.footer svg{width:5px;height:5px;fill:var(--white)}
.socials{margin-left:auto;display:flex;gap:2px;align-items:center}
.socials span{width:7px;height:7px;border-radius:50%;border:1px solid var(--white)}
.page-no{margin-left:8px;width:9px;height:9px;border-radius:50%;background:#3d2a57;font-size:4px;display:flex;align-items:center;justify-content:center}
.body-text{font-size:6.2px;line-height:11px;color:var(--ink);text-align:justify}
/* round photo areas */
.photo-round{position:absolute;border-radius:50%}
/* cover */
.cover{background:linear-gradient(160deg,#8a4fb0 0%,#a55db6 45%,#9c5ab5 70%,#6d4aa8 100%)}
.cover .brand{left:37px;top:42px;color:var(--white)}
.cover .brand-dot{width:22px;height:22px}
.cover .brand-name{font-size:21px}
.cover .brand-tag{font-size:7px;opacity:.9}
.cover-title{left:37px;top:108px;font-family:var(--serif);font-size:16px;line-height:22px;color:var(--white);font-weight:400}
.cover-lead{left:37px;top:158px;width:170px;font-size:7px;line-height:11px;color:var(--white);text-align:justify}
.cover-date{left:37px;top:203px;font-size:7px;color:var(--white);display:flex;gap:4px;align-items:center;font-weight:500}
.cover-photo{left:236px;top:26px;width:198px;height:198px;border:2px solid var(--white);
  background:linear-gradient(135deg,#eef0f2 0%,#d9c4b8 50%,#a9a6ad 100%)}
/* mission */
.mission-ring{left:10px;top:14px;width:206px;height:206px;border:1.5px solid var(--plum)}
.mission-photo{left:20px;top:24px;width:186px;height:186px;
  background:linear-gradient(135deg,#3f4a2e 0%,#8a2a25 50%,#6e5a4c 100%)}
/* metrics */
.metric-text{left:77px;width:133px;font-size:6.4px;line-height:11px;color:var(--ink);text-align:justify}
/* program cards */
.card{position:absolute;top:72px;width:126px;height:136px;background:var(--white);border:1px solid #ddd2e8;border-radius:3px}
.card-photo{position:absolute;left:4px;top:4px;width:117px;height:65px;border-radius:2px}
.price{position:absolute;right:-4px;top:-7px;width:27px;height:27px;border-radius:50%;background:var(--plum);
  border:2px solid var(--white);color:var(--white);font-size:8px;font-weight:500;display:flex;align-items:center;justify-content:center}
.card h3{position:absolute;left:13px;top:80px;width:100px;font-size:6.6px;line-height:9.5px;font-weight:500;color:var(--ink)}
.card p{position:absolute;left:13px;width:100px;font-size:4.8px;line-height:8px;color:var(--muted);text-align:justify}
/* testimonials */
.quote{position:absolute;width:130px;height:64px;background:var(--white);border:1px solid #e2d8ec;border-radius:2px;padding:9px 11px 0}
.quote p{font-size:4.6px;line-height:7.5px;color:var(--ink);text-align:justify}
.quote .by{margin-top:3px;font-size:4.8px;display:flex;gap:7px;align-items:center}
.quote .by b{color:var(--plum);font-weight:500}
.quote .stars{color:var(--gold);letter-spacing:1px;font-size:5px}
.avatar{position:absolute;width:16px;height:16px;border-radius:50%;border:1.5px solid var(--white);background:linear-gradient(135deg,#9b8aa8,#5e5266)}
/* closing */
.closing{background:linear-gradient(120deg,#c06ab6 0%,#a462b8 45%,#8357ad 100%)}
.closing .brand{left:50%;top:52px;transform:translateX(-50%);color:var(--white)}
.closing .brand-dot{width:20px;height:20px}
.closing .brand-name{font-size:20px}
.closing .brand-tag{font-size:6.4px}
.thanks{left:0;width:100%;top:112px;text-align:center;font-family:var(--serif);font-size:31px;color:var(--white)}
.closing-contact{left:0;width:100%;top:160px;display:flex;justify-content:center;gap:16px;color:var(--white);font-size:8.5px}
.closing-contact span{display:flex;align-items:center;gap:5px}
.closing-contact svg{width:8px;height:8px;fill:var(--white)}
.closing .socials{position:absolute;left:50%;top:188px;transform:translateX(-50%);gap:4px}
.closing .socials span{width:12px;height:12px}
</style>
</head>
<body>

<!-- Cover -->
<section class="slide cover col-a row-1">
  <div class="brand"><span class="brand-dot"></span><div><div class="brand-name">Marigold Haven</div><div class="brand-tag">Pregnancy &amp; Family Support</div></div></div>
  <h1 class="abs cover-title">A Web of Support<br>When It’s Needed Most</h1>
  <p class="abs cover-lead">Marigold Haven exists to walk alongside families navigating pregnancy complications, loss, and uncertainty—so no one has to go through it alone.</p>
  <div class="abs cover-date"><svg width="7" height="7" viewBox="0 0 10 10"><rect x="1" y="2" width="8" height="7" fill="none" stroke="#fff" stroke-width="1.2"/><line x1="1" y1="4" x2="9" y2="4" stroke="#fff"/></svg>April 03,2026</div>
  <div class="photo-round cover-photo" role="img" aria-label="Photo of a smiling pregnant woman on the phone"></div>
</section>

<!-- Key Metrics -->
<section class="slide col-b row-1">
  <h2 class="slide-title">Key Metrics</h2>
  <div class="brand brand-sm"><span class="brand-dot"></span><div><div class="brand-name">Marigold Haven</div><div class="brand-tag">Pregnancy &amp; Family Support</div></div></div>
  <svg class="abs" style="left:0;top:0" width="447" height="251" viewBox="0 0 447 251">
    <defs><g id="tickBadge">
      <polygon points="0,-15 13,-7.5 13,7.5 0,15 -13,7.5 -13,-7.5" fill="#7b4fa6"/>
      <polyline points="-4,0 -1,3 5,-3" fill="none" stroke="#fff" stroke-width="1.6"/>
    </g></defs>
    <use href="#tickBadge" x="47" y="73"/><use href="#tickBadge" x="47" y="127"/><use href="#tickBadge" x="47" y="181"/>
    <g font-family="Roboto, sans-serif" font-size="4" fill="#3b3346" text-anchor="end">
      <text x="259" y="52">10</text><text x="259" y="66">9</text><text x="259" y="80">8</text><text x="259" y="94">7</text><text x="259" y="108">6</text><text x="259" y="122">5</text><text x="259" y="136">4</text><text x="259" y="150">3</text><text x="259" y="164">2</text><text x="259" y="178">1</text><text x="259" y="192">0</text>
    </g>
    <line x1="264" y1="48" x2="264" y2="191" stroke="#9c93a8" stroke-width=".5"/>
    <line x1="264" y1="191" x2="431" y2="191" stroke="#9c93a8" stroke-width=".5"/>
    <rect x="274.5" y="128" width="11" height="63" fill="#b99ad6"/>
    <rect x="301.5" y="121" width="11" height="70" fill="#7b4fa6"/>
    <rect x="328.5" y="91.6" width="11" height="99.4" fill="#b99ad6"/>
    <rect x="354.5" y="121" width="11" height="70" fill="#7b4fa6"/>
    <rect x="381.5" y="128" width="11" height="63" fill="#b99ad6"/>
    <rect x="408.5" y="91.6" width="11" height="99.4" fill="#7b4fa6"/>
    <g font-family="Roboto, sans-serif" font-size="4" fill="#3b3346" text-anchor="middle">
      <text x="280" y="125">4.5%</text><text x="307" y="118">5%</text><text x="334" y="88">7.1%</text><text x="360" y="118">5%</text><text x="387" y="125">4.5%</text><text x="414" y="88">7.1%</text>
      <text x="280" y="198">2000</text><text x="307" y="198">2005</text><text x="334" y="198">2010</text><text x="360" y="198">2015</text><text x="387" y="198">2020</text><text x="414" y="198">2024</text>
    </g>
  </svg>
  <p class="abs metric-text" style="top:54px">Sed ut perspiciatis unde omnis iste natus error sitaccudoloremque laudantium, totam rem apaque ipsa qure vtae vit explicabo.</p>
  <p class="abs metric-text" style="top:108px">Sed ut perspiciatis unde omnis iste natus error sitaccudoloremque laudantium, totam rem apaque ipsa qure vtae vit explicabo.</p>
  <p class="abs metric-text" style="top:162px">Sed ut perspiciatis unde omnis iste natus error sitaccudoloremque laudantium, totam rem apaque ipsa qure vtae vit explicabo.</p>
  <footer class="footer"><span class="item"><svg viewBox="0 0 10 10"><rect x="0" y="2" width="10" height="6"/></svg>hello@marigoldhavencare.org</span><span class="item"><svg viewBox="0 0 10 10"><path d="M1 1h3l1 3-2 1a6 6 0 0 0 2 2l1-2 3 1v3c-5 0-8-3-8-8z"/></svg>+1 555 014 2290</span><span class="socials"><span></span><span></span><span></span><span></span><span></span></span><span class="page-no">05</span></footer>
</section>

<!-- Our Mission -->
<section class="slide col-a row-2">
  <div class="brand brand-sm"><span class="brand-dot"></span><div><div class="brand-name">Marigold Haven</div><div class="brand-tag">Pregnancy &amp; Family Support</div></div></div>
  <div class="photo-round mission-ring"></div>
  <div class="photo-round mission-photo" role="img" aria-label="Photo of a baby footprint keepsake beneath a decorated tree"></div>
  <h2 class="abs" style="left:235px;top:31px;font-family:var(--serif);font-size:17px;font-weight:400;color:var(--plum)">Our Mission</h2>
  <p class="abs body-text" style="left:235px;top:62px;width:183px">Marigold Haven was created from lived experience—and a deep calling to support families during moments of profound uncertainty. Marigold Haven’s story is woven into the very foundation of this work. During a complicated pregnancy marked by prolonged hospital stays, unanswered questions, and long stretches of waiting, our family experienced firsthand how isolating this season can feel. Even with excellent medical care, there were moments when support felt fragmented—when emotional weight, practical needs, and financial uncertainty all collided at once. She was lovingly known as our little sunshine. In a moment filled with so much pain, when we were finally able to see her—her tiny hands</p>
  <footer class="footer"><span class="item"><svg viewBox="0 0 10 10"><rect x="0" y="2" width="10" height="6"/></svg>hello@marigoldhavencare.org</span><span class="item"><svg viewBox="0 0 10 10"><path d="M1 1h3l1 3-2 1a6 6 0 0 0 2 2l1-2 3 1v3c-5 0-8-3-8-8z"/></svg>+1 555 014 2290</span><span class="socials"><span></span><span></span><span></span><span></span><span></span></span><span class="page-no">02</span></footer>
</section>

<!-- Partnership -->
<section class="slide col-b row-2">
  <h2 class="slide-title" style="top:11px">Partnership</h2>
  <div class="brand brand-sm"><span class="brand-dot"></span><div><div class="brand-name">Marigold Haven</div><div class="brand-tag">Pregnancy &amp; Family Support</div></div></div>
  <svg class="abs" style="left:0;top:0" width="447" height="251" viewBox="0 0 447 251">
    <defs><polygon id="hexTile" points="0,-35 30,-17.5 30,17.5 0,35 -30,17.5 -30,-17.5" fill="#fff" stroke="#e2d6ee" stroke-width=".8"/></defs>
    <g>
      <use href="#hexTile" x="64" y="74"/><use href="#hexTile" x="128" y="74"/><use href="#hexTile" x="192" y="74"/><use href="#hexTile" x="256" y="74"/><use href="#hexTile" x="320" y="74"/><use href="#hexTile" x="384" y="74"/>
      <use href="#hexTile" x="96" y="131"/><use href="#hexTile" x="160" y="131"/><use href="#hexTile" x="224" y="131"/><use href="#hexTile" x="288" y="131"/><use href="#hexTile" x="352" y="131"/>
      <use href="#hexTile" x="128" y="186"/><use href="#hexTile" x="192" y="186"/><use href="#hexTile" x="256" y="186"/><use href="#hexTile" x="320" y="186"/>
    </g>
    <g font-family="Roboto, sans-serif" font-size="7" font-weight="500" fill="#2b2530" text-anchor="middle">
      <text x="64" y="76.5">Lumen Co</text><text x="128" y="76.5">Orbitra</text><text x="192" y="76.5">Crestline</text><text x="256" y="76.5">Nimbus</text><text x="320" y="76.5">Fernway</text><text x="384" y="76.5">Valora</text>
      <text x="96" y="133.5">Kestrel</text><text x="160" y="133.5">Humanis</text><text x="224" y="133.5">Tallow &amp; Co</text><text x="288" y="133.5">Harborly</text><text x="352" y="133.5">Ringwell</text>
      <text x="128" y="188.5">Monarch</text><text x="192" y="188.5">Alder</text><text x="256" y="188.5">Quillon</text><text x="320" y="188.5">Brookline</text>
    </g>
  </svg>
  <footer class="footer"><span class="item"><svg viewBox="0 0 10 10"><rect x="0" y="2" width="10" height="6"/></svg>hello@marigoldhavencare.org</span><span class="item"><svg viewBox="0 0 10 10"><path d="M1 1h3l1 3-2 1a6 6 0 0 0 2 2l1-2 3 1v3c-5 0-8-3-8-8z"/></svg>+1 555 014 2290</span><span class="socials"><span></span><span></span><span></span><span></span><span></span></span><span class="page-no">06</span></footer>
</section>

<!-- Program Overview -->
<section class="slide col-a row-3">
  <h2 class="slide-title">Program Overview</h2>
  <div class="brand brand-sm"><span class="brand-dot"></span><div><div class="brand-name">Marigold Haven</div><div class="brand-tag">Pregnancy &amp; Family Support</div></div></div>
  <p class="abs body-text" style="left:26px;top:36px;width:300px;font-size:6.6px">Marigold Haven supports families with thoughtfully curated care packages designed to provide grounding, relief, and reassurance during extended hospital stays.</p>
  <article class="card" style="left:26px">
    <div class="card-photo" role="img" aria-label="Photo of a family running through a field at sunset" style="background:linear-gradient(180deg,#6d7fa8 0%,#e7b04a 55%,#6f6a2a 100%)"></div>
    <span class="price">$50</span>
    <h3>Comfort Essentials For<br>One Family</h3>
    <p style="top:104px">Provides items like a soft blanket, self-care essentials, and a handwritten note to bring comfort during a difficult moment.</p>
  </article>
  <article class="card" style="left:157px">
    <div class="card-photo" role="img" aria-label="Photo of an expecting couple relaxing at home" style="background:linear-gradient(135deg,#e8e6e4 0%,#c9c0bb 50%,#8b93a6 100%)"></div>
    <span class="price">$100</span>
    <h3>A Full Care Package</h3>
    <p style="top:94px">Supports families during extended hospital stays or those experiencing loss with thoughtful, practical essentials.</p>
  </article>
  <article class="card" style="left:288px">
    <div class="card-photo" role="img" aria-label="Photo of a large multigenerational group of families" style="background:linear-gradient(135deg,#8a9a6e 0%,#c8a06a 50%,#6d5a78 100%)"></div>
    <span class="price">$250</span>
    <h3>Support Multiple Families</h3>
    <p style="top:94px">Helps us reach more families in crisis while building and expanding our support program.</p>
  </article>
  <footer class="footer"><span class="item"><svg viewBox="0 0 10 10"><rect x="0" y="2" width="10" height="6"/></svg>hello@marigoldhavencare.org</span><span class="item"><svg viewBox="0 0 10 10"><path d="M1 1h3l1 3-2 1a6 6 0 0 0 2 2l1-2 3 1v3c-5 0-8-3-8-8z"/></svg>+1 555 014 2290</span><span class="socials"><span></span><span></span><span></span><span></span><span></span></span><span class="page-no">03</span></footer>
</section>

<!-- Testimonials -->
<section class="slide col-b row-3">
  <h2 class="slide-title">Testimonials</h2>
  <div class="brand brand-sm"><span class="brand-dot"></span><div><div class="brand-name">Marigold Haven</div><div class="brand-tag">Pregnancy &amp; Family Support</div></div></div>

  <div class="quote" style="left:24px;top:39px"><p>“Sed ut perspiciatis unde omnis iste natus error sitaccudoloremque laudantium, totam rem apaque ipsa qure vtae ue laudantium, totam rem apaque la ipsa qure vit explicabo”</p><div class="by"><span>~<b>Jane Rowe</b>,Customer</span><span class="stars">★★★★★</span></div></div>
  <div class="quote" style="left:159px;top:39px"><p>“Sed ut perspiciatis unde omnis iste natus error sitaccudoloremque laudantium, totam rem apaque ipsa qure vtae ue laudantium, totam rem apaque la ipsa qure vit explicabo”</p><div class="by"><span>~<b>Jane Rowe</b>,Customer</span><span class="stars">★★★★★</span></div></div>
  <div class="quote" style="left:294px;top:39px"><p>“Sed ut perspiciatis unde omnis iste natus error sitaccudoloremque laudantium, totam rem apaque ipsa qure vtae ue laudantium, totam rem apaque la ipsa qure vit explicabo”</p><div class="by"><span>~<b>Jane Rowe</b>,Customer</span><span class="stars">★★★★★</span></div></div>
  <div class="avatar" role="img" aria-label="Customer portrait" style="left:82px;top:113px"></div>
  <div class="avatar" role="img" aria-label="Customer portrait" style="left:217px;top:113px"></div>
  <div class="avatar" role="img" aria-label="Customer portrait" style="left:352px;top:113px"></div>

  <div class="quote" style="left:24px;top:135px"><p>“Sed ut perspiciatis unde omnis iste natus error sitaccudoloremque laudantium, totam rem apaque ipsa qure vtae ue laudantium, totam rem apaque la ipsa qure vit explicabo”</p><div class="by"><span>~<b>Jane Rowe</b>,Customer</span><span class="stars">★★★★★</span></div></div>
  <div class="quote" style="left:159px;top:135px"><p>“Sed ut perspiciatis unde omnis iste natus error sitaccudoloremque laudantium, totam rem apaque ipsa qure vtae ue laudantium, totam rem apaque la ipsa qure vit explicabo”</p><div class="by"><span>~<b>Jane Rowe</b>,Customer</span><span class="stars">★★★★★</span></div></div>
  <div class="quote" style="left:294px;top:135px"><p>“Sed ut perspiciatis unde omnis iste natus error sitaccudoloremque laudantium, totam rem apaque ipsa qure vtae ue laudantium, totam rem apaque la ipsa qure vit explicabo”</p><div class="by"><span>~<b>Jane Rowe</b>,Customer</span><span class="stars">★★★★★</span></div></div>
  <div class="avatar" role="img" aria-label="Customer portrait" style="left:82px;top:208px"></div>
  <div class="avatar" role="img" aria-label="Customer portrait" style="left:217px;top:208px"></div>
  <div class="avatar" role="img" aria-label="Customer portrait" style="left:352px;top:208px"></div>
  <footer class="footer"><span class="item"><svg viewBox="0 0 10 10"><rect x="0" y="2" width="10" height="6"/></svg>hello@marigoldhavencare.org</span><span class="item"><svg viewBox="0 0 10 10"><path d="M1 1h3l1 3-2 1a6 6 0 0 0 2 2l1-2 3 1v3c-5 0-8-3-8-8z"/></svg>+1 555 014 2290</span><span class="socials"><span></span><span></span><span></span><span></span><span></span></span><span class="page-no">07</span></footer>
</section>

<!-- Section Divider -->
<section class="slide col-a row-4">
  <h2 class="slide-title">Section Divider Title</h2>
  <div class="brand brand-sm"><span class="brand-dot"></span><div><div class="brand-name">Marigold Haven</div><div class="brand-tag">Pregnancy &amp; Family Support</div></div></div>
  <footer class="footer"><span class="item"><svg viewBox="0 0 10 10"><rect x="0" y="2" width="10" height="6"/></svg>hello@marigoldhavencare.org</span><span class="item"><svg viewBox="0 0 10 10"><path d="M1 1h3l1 3-2 1a6 6 0 0 0 2 2l1-2 3 1v3c-5 0-8-3-8-8z"/></svg>+1 555 014 2290</span><span class="socials"><span></span><span></span><span></span><span></span><span></span></span><span class="page-no">04</span></footer>
</section>

<!-- Closing / Call to action -->
<section class="slide closing col-b row-4" role="img" aria-label="Soft-tinted photo of a smiling woman in the background">
  <div class="brand"><span class="brand-dot"></span><div><div class="brand-name">Marigold Haven</div><div class="brand-tag">Pregnancy &amp; Family Support</div></div></div>
  <div class="abs thanks">Thank You</div>
  <div class="abs closing-contact">
    <span><svg viewBox="0 0 10 10"><rect x="0" y="2" width="10" height="6"/></svg>hello@marigoldhavencare.org</span>
    <span><svg viewBox="0 0 10 10"><path d="M1 1h3l1 3-2 1a6 6 0 0 0 2 2l1-2 3 1v3c-5 0-8-3-8-8z"/></svg>+1 555 014 2290</span>
  </div>
  <div class="socials"><span></span><span></span><span></span><span></span><span></span></div>
</section>

</body>
</html>
```